Soccer (Football) travel website

I need a responsive 1-page website design for a vacation/trip review website, plus a basic logo. The site's name is GlobeKickJourneys.com.

A site I have in mind is VoyagePanel.com:

https://www.voyagepanel.com/sailto/sailroutes.cfm?port=149&startDate=2019-08

Target Market(s)

Landing page used to attract people after they've clicked on an advertisement

Industry/Entity Type

Travel

Logo Text

GlobeKickJourneys.com

Number of Pages Required

1 page

Font styles to use
Sans Serif

Colors

Designer to choose colors to be used in the design.

Requirements
Must have
• A header that takes up very little vertical space.
• I've attached one file. This is what the content will consist of in the center of the site: a photo of a stadium with some description text below it.
Nice to have
• Needs to have a simple nav plus links for social media and newsletter

```html
<!DOCTYPE html>
<html lang="en">
<head>
<meta charset="utf-8">
<title>GlobeKickJourneys.com – Find Your Tour</title>
<link href="https://fonts.googleapis.com/css2?family=Lato:wght@300;400;700;900&display=swap" rel="stylesheet">
<style>
  :root {
    --blue: #2c6a92;
    --blue-sky: #5d9ec8;
    --blue-deep: #3c7fae;
    --orange: #ff5722;
    --orange-soft: #ff8a3d;
    --yellow: #fbc02d;
    --text: #555a5e;
    --line: #e6e8ea;
    --white: #ffffff;
    --pitch: #3f7a45;
    --stand: #4f6f94;
    --grey-icon: #c9cccf;
  }
  * { box-sizing: border-box; margin: 0; padding: 0; }
  html, body { width: 1200px; height: 2239px; overflow: hidden; }
  body {
    position: relative;
    font-family: 'Lato', sans-serif;
    color: var(--text);
    background: var(--white);
  }

  /* Hero */
  .hero { position: absolute; left: 0; top: 0; width: 1200px; height: 445px; overflow: hidden; }
  .hero-backdrop { position: absolute; inset: 0; }
  .brand {
    position: absolute; display: flex; align-items: center; gap: 12px;
    font-weight: 700; font-size: 30px; color: var(--blue); letter-spacing: 0.2px;
  }
  .brand-dot { width: 32px; height: 32px; border-radius: 50%; background: var(--orange); flex: none; }
  .hero .brand { left: 176px; top: 38px; }
  .search {
    position: absolute; left: 727px; top: 37px; width: 186px; height: 36px;
    border: 1.5px solid var(--white); border-radius: 18px;
    display: flex; align-items: center; justify-content: space-between;
    padding: 0 14px; color: var(--white); font-size: 12px;
  }
  .menu {
    position: absolute; left: 960px; top: 45px; display: flex; align-items: center; gap: 10px;
    color: var(--white); font-size: 13px; font-weight: 700; letter-spacing: 0.5px;
  }
  .hero-title { position: absolute; left: 185px; top: 192px; color: var(--blue); line-height: 0.98; }
  .hero-title .light { display: block; font-weight: 300; font-size: 78px; }
  .hero-title .bold { display: block; font-weight: 900; font-size: 78px; letter-spacing: 1px; }
  .scroll-hint { position: absolute; left: 588px; top: 360px; }

  /* Section headings */
  .section-title {
    position: absolute; left: 0; width: 1200px; text-align: center;
    color: var(--orange); font-weight: 300; font-size: 32px;
  }

  /* Featured */
  .featured-card { position: absolute; top: 560px; width: 273px; text-align: center; }
  .stadium-photo { background: linear-gradient(180deg, #8ea6c0 0%, var(--stand) 32%, var(--pitch) 55%, #5d9a52 100%); }
  .featured-card .stadium-photo { width: 273px; height: 165px; }
  .featured-card h3 { margin-top: 27px; font-weight: 400; font-size: 19px; color: var(--blue); }
  .featured-card p { margin-top: 8px; font-size: 13.5px; line-height: 17px; font-weight: 300; padding: 0 4px; }

  /* Testimonial */
  .testimonial {
    position: absolute; left: 0; top: 894px; width: 1200px; height: 319px;
    background: var(--orange); color: var(--white); text-align: center;
  }
  .testimonial-pattern { position: absolute; inset: 0; background: radial-gradient(ellipse at 15% 55%, rgba(255,160,50,.45), transparent 45%), radial-gradient(ellipse at 85% 40%, rgba(255,160,50,.35), transparent 45%); }
  .testimonial h2 { position: absolute; top: 54px; width: 100%; font-weight: 400; font-size: 32px; }
  .testimonial blockquote {
    position: absolute; left: 240px; top: 122px; width: 720px;
    font-size: 22px; line-height: 29px; font-weight: 400;
  }
  .quote-mark { position: absolute; font-size: 110px; font-weight: 900; line-height: 1; font-family: 'Lato', sans-serif; }
  .quote-open { left: 188px; top: 92px; }
  .quote-close { left: 970px; top: 158px; }
  .dots { position: absolute; top: 243px; left: 0; width: 100%; display: flex; justify-content: center; gap: 11px; }
  .dots span { width: 12px; height: 12px; border-radius: 50%; background: var(--white); }
  .dots .active { background: var(--yellow); }

  /* Best tours */
  .tour-card {
    position: absolute; left: 160px; width: 880px; height: 204px;
    border: 3px solid var(--line); border-radius: 8px; background: var(--white);
  }
  .tour-card .stadium-photo { position: absolute; left: 13px; top: 28px; width: 273px; height: 154px; }
  .tour-info { position: absolute; left: 303px; top: 30px; width: 405px; }
  .tour-length { font-size: 12px; color: var(--orange); font-weight: 400; }
  .tour-info h3 { margin-top: 3px; font-size: 19px; font-weight: 400; color: var(--blue); }
  .tour-info p { margin-top: 4px; font-size: 13.5px; line-height: 17px; font-weight: 300; }
  .rating { margin-top: 10px; display: flex; gap: 4px; }
  .rating span { width: 12px; height: 12px; border-radius: 50%; border: 2px solid var(--blue-deep); }
  .rating .on { background: var(--blue-deep); }
  .booking {
    position: absolute; left: 731px; top: 71px; width: 126px; height: 36px;
    border: 1.5px solid var(--blue-deep); border-radius: 18px;
    display: flex; align-items: center; justify-content: center; gap: 8px;
    color: var(--blue-deep); font-size: 12px; letter-spacing: 0.5px;
  }
  .price-alert {
    position: absolute; left: 744px; top: 132px; display: flex; align-items: center; gap: 8px;
    color: var(--blue-deep); font-size: 11px;
  }

  /* Footer */
  .footer { position: absolute; left: 0; top: 2010px; width: 1200px; height: 229px; }
  .footer-pattern { position: absolute; inset: 0; background: radial-gradient(ellipse at 20% 95%, rgba(251,192,45,.35), transparent 30%), radial-gradient(ellipse at 90% 60%, rgba(255,138,61,.3), transparent 30%); }
  .footer .brand { left: 182px; top: 74px; }
  .social { position: absolute; left: 900px; top: 81px; display: flex; gap: 15px; }
  .social span { width: 24px; height: 24px; border-radius: 50%; background: var(--grey-icon); }
</style>
</head>
<body>

<header class="hero">
  <svg class="hero-backdrop" role="img" aria-label="Faceted blue backdrop with scattered orange and yellow confetti triangles" width="1200" height="445" viewBox="0 0 1200 445">
    <defs>
      <linearGradient id="skyFill" x1="0" y1="0" x2="1" y2="1">
        <stop offset="0" stop-color="#4e92c0"/>
        <stop offset="1" stop-color="#6aa8d0"/>
      </linearGradient>
    </defs>
    <polygon points="686,0 1200,0 1200,445 552,445 620,224" fill="url(#skyFill)"/>
  </svg>

  <div class="brand"><span class="brand-dot"></span>GlobeKickJourneys</div>

  <div class="search">
    <span>Search...</span>
    <svg width="16" height="16" viewBox="0 0 16 16" fill="none" stroke="#fff" stroke-width="1.5"><circle cx="6.5" cy="6.5" r="5"/><line x1="10.5" y1="10.5" x2="15" y2="15"/></svg>
  </div>

  <nav class="menu">
    <svg width="16" height="12" viewBox="0 0 16 12" stroke="#fff" stroke-width="1.6"><line x1="0" y1="1" x2="16" y2="1"/><line x1="0" y1="6" x2="16" y2="6"/><line x1="0" y1="11" x2="16" y2="11"/></svg>
    MENU
  </nav>

  <h1 class="hero-title"><span class="light">Find Your</span><span class="bold">TOUR</span></h1>

  <svg class="scroll-hint" width="20" height="56" viewBox="0 0 20 56" fill="none" stroke="#fff" stroke-width="1.5">
    <rect x="1" y="1" width="18" height="30" rx="9"/>
    <line x1="10" y1="8" x2="10" y2="14"/>
    <polyline points="4,38 10,44 16,38"/>
    <polyline points="4,46 10,52 16,46"/>
  </svg>
</header>

<h2 class="section-title" style="top:485px">Featured Tours</h2>

<article class="featured-card" style="left:161px">
  <div class="stadium-photo" role="img" aria-label="Stadium interior with blue stands and green pitch"></div>
  <h3>MANCHESTER, NOVEMBER</h3>
  <p>Lorem ipsum dolor sit amet, consectetuer adipiscing elit cum sociis natoque socre penatibus et magnis dis parturient montes, nascetur ridiculus mus.</p>
</article>
<article class="featured-card" style="left:464px">
  <div class="stadium-photo" role="img" aria-label="Stadium interior with covered stands and green pitch"></div>
  <h3>LONDON, DECEMBER</h3>
  <p>Lorem ipsum dolor sit amet, consectetuer adipiscing elit cum sociis natoque socre penatibus et magnis dis parturient montes, nascetur ridiculus mus.</p>
</article>
<article class="featured-card" style="left:767px">
  <div class="stadium-photo" role="img" aria-label="Stadium interior with red seats and green pitch" style="background:linear-gradient(180deg,#c9ccd0 0%,#b8343a 30%,#a52a30 48%,#4c8a45 60%,#5f9d52 100%)"></div>
  <h3>LIBERPOOL, MARCH</h3>
  <p>Lorem ipsum dolor sit amet, consectetuer adipiscing elit cum sociis natoque socre penatibus et magnis dis parturient montes, nascetur ridiculus mus.</p>
</article>

<section class="testimonial">
  <div class="testimonial-pattern" role="img" aria-label="Scattered orange and yellow confetti triangles"></div>
  <h2>WHAT DO THEY SAY ABOUT US?</h2>
  <span class="quote-mark quote-open">&ldquo;</span>
  <blockquote>Lorem ipsum dolor sit amet, consectetuer adipiscing elit cum sociis natoque socre penatibus et magnis dis parturient montes, nascetur ridiculus mus.</blockquote>
  <span class="quote-mark quote-close">&rdquo;</span>
  <div class="dots"><span class="active"></span><span></span><span></span></div>
</section>

<h2 class="section-title" style="top:1258px">Best Tours</h2>

<article class="tour-card" style="top:1324px">
  <div class="stadium-photo" role="img" aria-label="Stadium interior with blue stands and green pitch"></div>
  <div class="tour-info">
    <div class="tour-length">1 Day</div>
    <h3>MANCHESTER, NOVEMBER</h3>
    <p>Lorem ipsum dolor sit amet, consectetuer adipiscing elit cum sociis natoque socre penatibus et magnis natoque socre penatibus et magnis natoque socre penatibus et magnis dis parturient montes, nascetur ridiculus mus.</p>
    <div class="rating"><span></span><span></span><span></span><span></span><span class="on"></span></div>
  </div>
  <div class="booking"><svg width="14" height="13" viewBox="0 0 14 13" fill="none" stroke="currentColor" stroke-width="1.2"><rect x="1" y="2" width="12" height="10" rx="1"/><line x1="1" y1="5" x2="13" y2="5"/></svg>BOOKING</div>
  <div class="price-alert"><svg width="11" height="12" viewBox="0 0 11 12" fill="none" stroke="#555" stroke-width="1.1"><path d="M2 9 V5 a3.5 3.5 0 0 1 7 0 V9 Z M1 9 H10 M4.5 11 H6.5"/></svg>Get Price Alerts</div>
</article>

<article class="tour-card" style="top:1548px">
  <div class="stadium-photo" role="img" aria-label="Stadium interior with blue stands and green pitch"></div>
  <div class="tour-info">
    <div class="tour-length">1 Day</div>
    <h3>MANCHESTER, NOVEMBER</h3>
    <p>Lorem ipsum dolor sit amet, consectetuer adipiscing elit cum sociis natoque socre penatibus et magnis natoque socre penatibus et magnis natoque socre penatibus et magnis dis parturient montes, nascetur ridiculus mus.</p>
    <div class="rating"><span></span><span></span><span></span><span></span><span class="on"></span></div>
  </div>
  <div class="booking"><svg width="14" height="13" viewBox="0 0 14 13" fill="none" stroke="currentColor" stroke-width="1.2"><rect x="1" y="2" width="12" height="10" rx="1"/><line x1="1" y1="5" x2="13" y2="5"/></svg>BOOKING</div>
  <div class="price-alert"><svg width="11" height="12" viewBox="0 0 11 12" fill="none" stroke="#555" stroke-width="1.1"><path d="M2 9 V5 a3.5 3.5 0 0 1 7 0 V9 Z M1 9 H10 M4.5 11 H6.5"/></svg>Get Price Alerts</div>
</article>

<article class="tour-card" style="top:1772px">
  <div class="stadium-photo" role="img" aria-label="Stadium interior with blue stands and green pitch"></div>
  <div class="tour-info">
    <div class="tour-length">1 Day</div>
    <h3>MANCHESTER, NOVEMBER</h3>
    <p>Lorem ipsum dolor sit amet, consectetuer adipiscing elit cum sociis natoque socre penatibus et magnis natoque socre penatibus et magnis natoque socre penatibus et magnis dis parturient montes, nascetur ridiculus mus.</p>
    <div class="rating"><span></span><span></span><span></span><span></span><span class="on"></span></div>
  </div>
  <div class="booking"><svg width="14" height="13" viewBox="0 0 14 13" fill="none" stroke="currentColor" stroke-width="1.2"><rect x="1" y="2" width="12" height="10" rx="1"/><line x1="1" y1="5" x2="13" y2="5"/></svg>BOOKING</div>
  <div class="price-alert"><svg width="11" height="12" viewBox="0 0 11 12" fill="none" stroke="#555" stroke-width="1.1"><path d="M2 9 V5 a3.5 3.5 0 0 1 7 0 V9 Z M1 9 H10 M4.5 11 H6.5"/></svg>Get Price Alerts</div>
</article>

<footer class="footer">
  <div class="footer-pattern" role="img" aria-label="Scattered orange and yellow confetti triangles"></div>
  <div class="brand"><span class="brand-dot"></span>GlobeKickJourneys</div>
  <div class="social" aria-label="Social media links"><span></span><span></span><span></span></div>
</footer>

</body>
</html>
```